Bold & Modern "Save the Date" Design for Medical Yacht Brunch Event

We are looking for a bold, modern, and eye-catching "Save the Date" design for a physician brunch event.
Event Overview:
This is a 2-hour brunch aboard a luxury yacht, hosted for a select group of physician investigators participating in our new VERANT study. The event will take place during the upcoming OLMQ medical conference.
Event Name:
VERANT Study Network Forum
Date:
Saturday, July 19th (9:30am - 11:30am)
Location:
Nori Belle yacht (docked directly outside of the Calderwynne)
Blurb:
Join us aboard Nori Belle for a VERANT Study Investigator Brunch during OLMQ 2025.
Hosted by TORQA, this 2-hour event brings together physicians to discuss the future of VERANT in a waterfront setting.
Audience:
Physicians in the pain management and medical device space. The tone should be sophisticated and professional, but elevated and engaging—not clinical or bland.
Design Requirements:
Bold and modern visual style that grabs attention
Must include the TORQA logo (primary brand) and ZELO CORE TQ logo (subsidiary)
Include the OLMQ conference logo to indicate the event alignment
Reflect our TORQA brand colors, with bonus points for incorporating complementary elements of ZELO CORE TQ’s color palette
Layout should highlight that this is a “Save the Date” for a VERANT Study investigator brunch aboard a yacht
Design should feel exclusive and premium, but still professional
We will provide all logos and branding guidelines. The final design will be used in both digital and printed formats. Looking for a clean layout with strong typography and sleek design elements.
Physicians
Medical Device

```html
<!DOCTYPE html>
<html lang="en">
<head>
<meta charset="utf-8">
<title>VERANT Study Network Forum – Save the Date</title>
<link rel="stylesheet" href="https://fonts.googleapis.com/css2?family=Italiana&family=Jost:ital,wght@0,400;0,500;0,600;0,700;1,400&display=swap">
<style>
:root{
  --paper:#fdf7f8;
  --forest:#3f6a2c;
  --leaf:#62a83c;
  --lime:#9ecf5f;
  --navy:#001840;
  --white:#ffffff;
}
*{margin:0;padding:0;box-sizing:border-box}
html,body{width:851px;height:1200px;overflow:hidden;background:var(--paper)}
.card{position:relative;width:851px;height:1200px;background:var(--paper);font-family:"Jost",sans-serif;overflow:hidden}
.backdrop{position:absolute;inset:0;width:851px;height:1200px}
.content{position:absolute;inset:0}
.title{position:absolute;top:110px;left:0;width:100%;text-align:center;font-weight:700;font-size:42px;color:var(--forest);letter-spacing:0.2px}
.headline{font-family:"Italiana",serif;color:var(--forest);position:absolute;line-height:1}
.headline-save{top:168px;left:178px;font-size:222px}
.headline-the{top:374px;left:143px;font-size:72px}
.headline-date{top:354px;left:258px;font-size:222px}
.blurb{position:absolute;top:582px;left:0;width:100%;text-align:center;font-weight:600;font-size:16px;line-height:21px;color:var(--leaf)}
.audience-label{position:absolute;top:655px;left:0;width:100%;text-align:center;font-weight:600;font-size:23px;color:var(--leaf)}
.audience-text{position:absolute;top:688px;left:0;width:100%;text-align:center;font-weight:600;font-size:16.5px;color:var(--leaf)}
.when{position:absolute;top:752px;left:0;width:100%;text-align:center;color:var(--forest);font-weight:700;font-size:18.5px;letter-spacing:0.36em}
.when p{height:37px}
.where-label{position:absolute;top:908px;left:0;width:100%;text-align:center;color:var(--white);font-weight:600;font-size:23px}
.where-text{position:absolute;top:944px;left:0;width:100%;text-align:center;color:var(--white);font-style:italic;font-size:18px;letter-spacing:0.26em;line-height:27px}
.brands{position:absolute;top:1080px;left:0;width:100%;height:40px}
.brand{position:absolute;top:0;font-weight:600;line-height:40px}
.brand-primary{left:246px;font-size:30px;color:var(--leaf)}
.brand-badge{position:absolute;left:407px;top:-2px;width:42px;height:42px;border-radius:50%;background:#2f6fb8}
.brand-sub{left:508px;font-size:23px;color:var(--navy)}
</style>
</head>
<body>
<main class="card">
  <svg class="backdrop" viewBox="0 0 851 1200" aria-hidden="true">
    <path d="M851 501 C 800 700 640 888 316 894 L 851 894 Z" fill="var(--lime)"/>
    <rect x="0" y="894" width="453" height="306" fill="var(--navy)"/>
    <rect x="453" y="894" width="398" height="306" fill="var(--lime)"/>
  </svg>
  <div class="content">
    <h1 class="title">VERANT Study Network Forum</h1>
    <div class="headline headline-save">Save</div>
    <div class="headline headline-the">the</div>
    <div class="headline headline-date">Date</div>
    <p class="blurb">Join us aboard Nori Belle for a VERANT Study Investigator Brunch during OLMQ 2025.<br>Hosted by TORQA, this 2-hour event brings together physicians to discuss the future of VERANT<br>in a waterfront setting.</p>
    <h2 class="audience-label">Audience:</h2>
    <p class="audience-text">Physicians in the pain management and medical device space.</p>
    <div class="when">
      <p>19 JULY 2025</p>
      <p>SATURDAY</p>
      <p>(9:30AM - 11:30AM)</p>
    </div>
    <h2 class="where-label">LOCATION:</h2>
    <p class="where-text">Nori Belle yacht<br>(docked directly outside of the Calderwynne)</p>
    <div class="brands">
      <span class="brand brand-primary">TORQA</span>
      <span class="brand-badge" role="img" aria-label="OLMQ 2025 conference badge"></span>
      <span class="brand brand-sub">ZELO CORE TQ</span>
    </div>
  </div>
</main>
</body>
</html>
```